Candle company needs a label for candle

Looking for a designer to create my candle label. I am going to attach a few pictures of my vision for the label as well as my Company Logo and jar I have puchased. I'm going for the modern rustic feel but you are the designer and have full trust in your abilities. The label is going to be printed on Kraft paper (2x3) so looking for the font to be black. The candle label MUST include the following information:
Candle Birchway Co.
NO. 01: Eucalyptus + Spearmint
Handmade In NJ
Soy Wax
9oz

Industry/Entity Type

Candle Industry

Colors

Designer to choose colors to be used in the design.

Requirements
Should not have
• Any images

```html
<!DOCTYPE html>
<html lang="en">
<head>
<meta charset="utf-8">
<title>Candle Birchway Co. — Jar Label</title>
<link rel="stylesheet" href="https://fonts.googleapis.com/css2?family=Crimson+Text:wght@400&family=Mrs+Saint+Delafield&display=swap">
<style>
  :root {
    --kraft: #d49d79;
    --ink: #3b3b3b;
    --rule: 3px;
  }
  * { box-sizing: border-box; margin: 0; padding: 0; }
  html, body {
    width: 1200px;
    height: 1200px;
    overflow: hidden;
    background: var(--kraft);
  }
  .canvas {
    width: 1200px;
    height: 1200px;
    display: flex;
    align-items: center;
    justify-content: center;
    font-family: "Crimson Text", Georgia, serif;
    color: var(--ink);
  }
  .label {
    width: 1000px;
    height: 626px;
    border: var(--rule) solid var(--ink);
    display: grid;
    grid-template-rows: 377px 123px 1fr;
  }
  .brand-area {
    display: flex;
    align-items: center;
    justify-content: center;
    border-bottom: var(--rule) solid var(--ink);
  }
  .brand-name {
    font-size: 60px;
    font-weight: 400;
    line-height: 1;
  }
  .details-row {
    display: grid;
    grid-template-columns: 311px 1fr;
    border-bottom: var(--rule) solid var(--ink);
  }
  .wax {
    display: flex;
    align-items: center;
    justify-content: center;
    border-right: var(--rule) solid var(--ink);
    font-size: 36px;
  }
  .scent {
    display: flex;
    flex-direction: column;
    align-items: center;
    justify-content: center;
    padding-left: 40px;
  }
  .scent-number {
    font-size: 30px;
    line-height: 1;
    margin-bottom: -4px;
  }
  .scent-name {
    font-family: "Mrs Saint Delafield", cursive;
    font-size: 62px;
    line-height: 1;
    white-space: nowrap;
  }
  .footer-row {
    display: flex;
    align-items: center;
    padding: 0 0 0 104px;
    font-size: 36px;
  }
  .footer-rule {
    width: 300px;
    height: 2px;
    background: var(--ink);
    margin: 0 30px 0 54px;
  }
</style>
</head>
<body>
  <main class="canvas">
    <section class="label">
      <div class="brand-area">
        <span class="brand-name">Candle Birchway Co.</span>
      </div>
      <div class="details-row">
        <div class="wax">Soy Wax</div>
        <div class="scent">
          <span class="scent-number">NO. 01:</span>
          <span class="scent-name">Eucalyptus + Spearmint</span>
        </div>
      </div>
      <div class="footer-row">
        <span class="weight">9 oz</span>
        <span class="footer-rule"></span>
        <span class="origin">Handmade In NJ</span>
      </div>
    </section>
  </main>
</body>
</html>
```